GDFH Business Card

Looking for a business card design to incorporate our branding. We want to only use the colors listing in the Branding Package (attached).
Updates

Target Market(s)

People who need their phone or device fixed.

Industry/Entity Type

Electronics

Contact Information for Business Card

Please use:

Gadget Fix Haven LLC
4870 S Ridgecrest Pkwy
Suite 318
San Antonio, TX 78291

Wendell Thorsby, Store Manager

(210) 555-0147

Requirements
Must have
• Must include the colors that are contained within the Branding Package PDF file.

```html
<!DOCTYPE html>
<html lang="en">
<head>
<meta charset="utf-8">
<title>Gadget Fix Haven – Business Card</title>
<link rel="stylesheet" href="https://fonts.googleapis.com/css2?family=Open+Sans:wght@400;700&display=swap">
<style>
  :root {
    --brand-red: #d23a1c;
    --ink: #2b2b2b;
    --card-bg: #f7f7f6;
    --card-edge: #b9b9b9;
    --page-bg: #e4e4e2;
  }
  * { box-sizing: border-box; margin: 0; padding: 0; }
  html, body {
    width: 1200px; height: 970px; overflow: hidden;
    background: var(--page-bg);
    font-family: "Open Sans", Arial, sans-serif;
    color: var(--ink);
  }
  .card {
    position: absolute; left: 120px; top: 218px;
    width: 960px; height: 534px;
    background: var(--card-bg);
    border: 1.5px solid var(--card-edge);
    border-radius: 26px;
  }
  .brand {
    position: absolute; left: 182px; top: 102px;
    display: flex; align-items: center; gap: 26px;
  }
  .brand-square {
    width: 118px; height: 118px;
    background: var(--brand-red);
    border-radius: 14px;
  }
  .brand-name {
    font-size: 62px; font-weight: 400; color: var(--brand-red);
    letter-spacing: 0.5px; white-space: nowrap;
  }
  .person {
    position: absolute; right: 509px; top: 330px;
    text-align: right; white-space: nowrap;
  }
  .person-name {
    font-size: 27px; font-weight: 700; color: var(--brand-red);
    letter-spacing: 0.5px; line-height: 1.2;
  }
  .person-title { font-size: 21px; line-height: 1.3; }
  .address { margin-top: 24px; font-size: 21px; line-height: 1.5; }
  .divider {
    position: absolute; left: 477px; top: 334px;
    width: 2px; height: 126px; background: var(--brand-red);
  }
  .contact {
    position: absolute; left: 508px; top: 330px;
    list-style: none;
  }
  .contact li {
    display: flex; align-items: center; gap: 10px;
    font-size: 21px; line-height: 34.5px; white-space: nowrap;
  }
  .contact svg { width: 20px; height: 20px; fill: var(--brand-red); flex: none; }
</style>
</head>
<body>
  <div class="card">
    <div class="brand">
      <div class="brand-square"></div>
      <div class="brand-name">Gadget Fix Haven</div>
    </div>

    <div class="person">
      <p class="person-name">WENDELL THORSBY</p>
      <p class="person-title">Store Manager</p>
      <p class="address">4870 S Ridgecrest Pkwy, Suite 318<br>San Antonio, TX 78291</p>
    </div>

    <div class="divider"></div>

    <ul class="contact">
      <li>
        <svg viewBox="0 0 20 20" aria-hidden="true"><path d="M2 7c0-2 3-4 8-4s8 2 8 4v2h-4V7H6v2H2z"/><path d="M5 10h10l2 7H3z"/></svg>
        (210) 555-0147
      </li>
      <li>
        <svg viewBox="0 0 20 20" aria-hidden="true"><rect x="5" y="2" width="10" height="5"/><rect x="1" y="7" width="18" height="8" rx="1.5"/><rect x="5" y="13" width="10" height="5"/></svg>
        (210) 555-0148
      </li>
      <li>
        <svg viewBox="0 0 20 20" aria-hidden="true"><path d="M1 4h18v12H1z"/><path d="M1 4l9 7 9-7" fill="none" stroke="#f7f7f6" stroke-width="1.6"/></svg>
        info@gadgetfixhaven.com
      </li>
      <li>
        <svg viewBox="0 0 20 20" aria-hidden="true"><circle cx="10" cy="10" r="8.5"/><path d="M1.5 10h17M10 1.5c-3 3-3 14 0 17M10 1.5c3 3 3 14 0 17" fill="none" stroke="#f7f7f6" stroke-width="1.3"/></svg>
        www.gadgetfixhaven.com
      </li>
    </ul>
  </div>
</body>
</html>
```